quickpine website

I need the graphics and images created for a web site. I have settled on a layout but are open to alternatives

I have already purchased the images I want to use.

I want the graphics/design to really give the web site a lift without deviating from the core concept (which is lots of white space, clean looking)

I have further files to upload for use (another 4).

The link to the current web site that requires re-skinning is: http://www.tarvinmarketing.com.au/cgi-bin/xmlweb.cgi/scriptlet/quickpine?cms_section=quickpine&cms_name=home
Updates

I forgot to mention that I would the design elements of the various text boxes down the right hand side and along the bottom of the page to be improved.  At the moment they look very one dimensional and boring.

Thanks

All files have now been uploaded.

Hi Guys
Some great designs are coming through.  I thought I would share elements that I like for each for those of you who are prepared to tweek their submissions.

Design ID 27087
1. Used used the proper logo file supplied
2. Like the use of images and design of the various text boxes down the right hand side of the page
3.  I like the footer - but would maybe change some of the images used
4.  I like the navigation bar

Design ID 27265
1. Like the placement of icons up the top.  I think this concept would work if there were maybe three other icons up there as well

Design ID 27266
1.  Like the design elements of the various text boxes down the right hand side of the page
2.  Like the grey background strip down the right hand side of page

Key thing I would like improved:
1.  The style and use of text in the header/banner.  I also think it looks a little one dimensional

Thanks

Rgds
Dale

Target Market(s)

SME businesses

Number of Pages Required

1 page

Requirements
Must have
• 1. Header/Banner must replicate concept provided
2. Please check out this web site as it is the design inspiration and should heavily influence the final design (use of colour etc) - www.plovinstudio.com

```html
<!DOCTYPE html>
<html lang="en">
<head>
<meta charset="utf-8">
<title>quickpine – Reshaping Business</title>
<link href="https://fonts.googleapis.com/css2?family=Ubuntu:wght@300;400;500&family=Open+Sans:wght@400;600;700&display=swap" rel="stylesheet">
<style>
:root{
  --blue:#1f8fd3;
  --blue-deep:#0b74c4;
  --blue-light:#5cb8ec;
  --orange:#f08c00;
  --orange-light:#ffb52e;
  --ink:#222;
  --text:#3c3c3c;
  --grey-panel:#ececec;
  --grey-line:#d6d6d6;
  --footer:#6b6b6b;
  --footer-dark:#3a3a3a;
}
*{box-sizing:border-box;margin:0;padding:0}
html,body{width:688px;height:1200px;overflow:hidden;background:#fff}
body{position:relative;font-family:"Open Sans",Arial,sans-serif;color:var(--text)}
.abs{position:absolute}
.display{font-family:"Ubuntu",Arial,sans-serif}

/* header */
.header{left:0;top:0;width:688px;height:58px;background:linear-gradient(#fff,#f3f3f3)}
.header-rule{left:0;top:58px;width:688px;height:3px;background:#cfcfcf}
.logo{left:43px;top:17px;display:flex;align-items:center;gap:5px}
.logo-dot{width:22px;height:22px;border-radius:50%;background:var(--blue-deep)}
.logo-name{font-family:"Ubuntu",sans-serif;font-size:22px;font-weight:400;color:var(--blue);line-height:24px}
.nav a{position:absolute;top:24px;font-size:8.6px;font-weight:600;color:#111;text-decoration:none;line-height:10px;letter-spacing:-.1px}
.nav .home{left:234px;top:20px;width:46px;height:19px;border-radius:10px;background:linear-gradient(var(--orange-light),var(--orange));color:#fff;text-align:center;line-height:19px;font-weight:400}

/* banner */
.banner{left:0;top:61px;width:425px;height:131px;background:linear-gradient(160deg,#48aef0 0%,#1a87d8 55%,#0f72c4 100%)}
.banner-side{left:425px;top:61px;width:263px;height:131px;background:linear-gradient(160deg,#62bff2,#3aa0e4);border-left:1px solid #9fd6f6}
.banner h1{left:55px;top:71px;font-family:"Ubuntu",sans-serif;font-weight:500;font-size:37px;color:#f4f7fa;line-height:44px;letter-spacing:-.3px;text-shadow:0 1px 1px rgba(0,0,0,.2)}
.banner h1 span{font-weight:300}
.banner .intro{left:56px;top:116px;width:360px;font-family:"Ubuntu",sans-serif;font-weight:300;font-size:11.6px;line-height:16px;color:#173c5c}
.banner .intro b{font-weight:400;font-size:15.5px;color:#173c5c}
.banner .call{left:56px;top:158px;font-family:"Ubuntu",sans-serif;font-weight:300;font-size:10.5px;color:#fff;line-height:20px}
.banner .call b{font-weight:400;font-size:16px}
.service-icon{width:41px;height:44px;border-radius:8px;background:linear-gradient(#2c3f55,#0d1a28)}
.service-icon.globe{border-radius:50%;width:40px;height:40px;background:radial-gradient(circle at 40% 35%,#8fd0ff,#1c5fc2 70%,#0b2f6f)}
.service-title{font-family:"Ubuntu",sans-serif;font-size:20.5px;line-height:21px;color:#fff;font-weight:400}
.service-title span{display:block;font-weight:300;color:#eaf6ff}

/* breadcrumb */
.crumbs{left:0;top:192px;width:688px;height:22px;background:linear-gradient(#7a7a7a,#4d4d4d);font-size:6.4px;color:var(--orange);padding:7px 0 0 43px;line-height:8px}

/* main column */
.lead{left:43px;width:365px;font-family:"Ubuntu",sans-serif;font-size:12.3px;color:var(--blue);line-height:15px}
.strong{left:43px;top:270px;width:365px;font-size:8.1px;font-weight:700;color:#111;line-height:11.2px}
.body{left:43px;width:365px;font-size:6.9px;line-height:11.3px;color:#333}
.thumb{left:43px;width:102px;border:1px solid #cfcfcf}
.pill{height:18px;padding:0 8px;border:1px solid #d4d4d4;border-radius:4px;background:linear-gradient(#fdfdfd,#ececec);font-family:"Ubuntu",sans-serif;font-size:12.2px;color:var(--blue);line-height:17px;white-space:nowrap}
.svc-text{width:250px;font-size:6.9px;line-height:11.4px;color:#333}
.more{font-size:6.7px;font-weight:700;color:var(--orange);line-height:8px}

/* call-out tiles */
.tile{width:179px;height:106px;border-radius:4px;background:linear-gradient(#62c0f2,#2a9ee2 55%,#1d8dd4);box-shadow:0 2px 3px rgba(0,0,0,.35);border:1px solid #2b89c8;padding:6px 7px}
.tile h3{font-family:"Ubuntu",sans-serif;font-weight:400;font-size:27px;line-height:30px;color:#fff}
.tile p{font-family:"Ubuntu",sans-serif;font-weight:300;font-size:10px;line-height:12px;color:#0f3f66;margin-top:2px}
.tile p b{font-weight:400}
.tile small{display:block;position:absolute;left:0;right:0;bottom:10px;text-align:center;font-size:7px;line-height:11px;color:#fff}
.tile small b{font-weight:400;color:#0b3c68}

/* sidebar boxes */
.box{left:437px;width:207px;border:1px solid #dcdcdc;border-radius:5px;background:linear-gradient(#ececec,#fff 40%)}
.box.assess{background:linear-gradient(#fdf3d9,#fffdf7 30%);border-color:#f0dfae}
.box-title{font-family:"Ubuntu",sans-serif;font-size:15.5px;color:#222;line-height:20px}
.box-title b{font-weight:400;font-size:23px}
.label{font-size:7.8px;font-weight:700;color:#444;line-height:10px}
.input{left:520px;width:116px;height:18px;border:1px solid #bcbcbc;background:#fff}
.btn{height:17px;border-radius:6px;font-family:"Ubuntu",sans-serif;font-weight:300;font-size:10px;color:#fff;text-align:center;line-height:17px}
.btn.blue{background:linear-gradient(#58bdf2,#1883d0)}
.btn.orange{background:linear-gradient(var(--orange-light),var(--orange))}
.badge{left:446px;top:236px;width:27px;height:27px;border-radius:50%;background:radial-gradient(#ffc430,#f08c00)}
.looking li{position:absolute;left:449px;list-style:none;font-size:8.2px;color:var(--blue);line-height:10px;white-space:nowrap}
.looking li::before{content:"";display:inline-block;width:4px;height:4px;border-radius:50%;background:var(--orange);margin-right:8px;vertical-align:1px}
.media-item{left:451px;font-size:8.2px;color:var(--blue);line-height:11px;display:flex;gap:8px}
.media-item svg{flex:none;margin-top:1px}
.video{left:447px;top:706px;width:188px;height:157px;background:radial-gradient(circle at 60% 55%,#555,#161616 75%)}
.video-head{left:453px;top:712px;font-family:"Ubuntu",sans-serif;font-size:11.5px;color:#3fb2ef;line-height:14px;padding-left:34px}
.video-head .av{position:absolute;left:0;top:0;width:28px;height:28px;background:#1d97d9}
.video-head small{display:block;font-family:"Open Sans",sans-serif;font-size:6.5px;color:#fff}
.video-head small span{color:#3fb2ef}

/* footer */
.footer{left:0;top:1129px;width:688px;height:53px;background:linear-gradient(#7a7a7a,#5e5e5e)}
.footer .site{left:42px;top:9px;font-family:"Ubuntu",sans-serif;font-size:17px;color:#e8e8e8;line-height:20px}
.footer .contact{left:42px;top:33px;font-family:"Ubuntu",sans-serif;font-weight:300;font-size:8.2px;color:#c9c9c9;line-height:10px}
.footer nav a{position:absolute;top:33px;font-family:"Ubuntu",sans-serif;font-weight:300;font-size:8.3px;color:var(--orange-light);text-decoration:none;line-height:10px}
.footer nav a.map{font-weight:500}
.footer nav i{position:absolute;top:33px;font-style:normal;font-size:8px;color:#bbb;line-height:10px}
.legal{left:0;top:1182px;width:688px;height:18px;background:var(--footer-dark);font-size:6px;color:#8a8a8a;line-height:18px}
.bubble{height:20px;border-radius:10px;background:linear-gradient(var(--orange-light),var(--orange));border:1px solid #e7e7e7;font-family:"Ubuntu",sans-serif;font-size:8.4px;color:#5a2a00;text-align:center;line-height:18px;box-shadow:0 1px 2px rgba(0,0,0,.3)}
</style>
</head>
<body>

<!-- header -->
<div class="abs header"></div>
<div class="abs header-rule"></div>
<div class="abs logo"><span class="logo-dot"></span><span class="logo-name">quickpine</span></div>
<nav class="nav">
  <a class="home" href="#">HOME</a>
  <a href="#" style="left:297px">WHAT WE'RE WORKING ON</a>
  <a href="#" style="left:430px">ABOUT US</a>
  <a href="#" style="left:495px">MEDIA</a>
  <a href="#" style="left:547px">BLOG</a>
  <a href="#" style="left:593px">CONTACT</a>
</nav>

<!-- banner -->
<section class="banner-wrap">
  <div class="abs banner"></div>
  <div class="abs banner-side"></div>
  <div class="banner">
    <h1 class="abs" style="left:55px;top:71px">Reshaping <span>Business</span></h1>
    <p class="abs intro"><b>Quickpine</b> is a marketing agency specialising in marketing campaign design &amp; execution using traditional and digital media.</p>
    <p class="abs call">Call Now on <b>1300 482 650</b></p>
  </div>
  <div class="abs service-icon" style="left:449px;top:75px" role="img" aria-label="Television icon"></div>
  <div class="abs service-title" style="left:514px;top:73px">Video<span>Production</span></div>
  <div class="abs service-icon globe" style="left:449px;top:134px" role="img" aria-label="Globe icon"></div>
  <div class="abs service-title" style="left:514px;top:133px">Online digital<span>Solutions</span></div>
</section>

<div class="abs crumbs">HERE YOU CAN PUT BREADCRUMBS IF YOUR SITE HAS SECONDS LEVELS</div>

<!-- main content -->
<main>
  <h2 class="abs lead" style="top:229px">At quickpine marketing we're reshaping business and building brands.</h2>
  <p class="abs strong">We're helping businesses like yours build their customer base and penetrate new markets.&nbsp; Quickpine achieve this through strategic market campaign design and execution using a combination of traditional and digital media.</p>
  <h2 class="abs lead" style="top:312px">We're your outsourced marketing department.</h2>
  <p class="abs body" style="top:338px">As your outsourced marketing managers, quickpine specialise in providing marketing strategies, brand &amp; logo development, public relations campaigns, advertising strategies, social media strategies, web site design and online marketing strategies.</p>
  <h2 class="abs lead" style="top:379px">We cause gravity to your business.</h2>
  <p class="abs body" style="top:406px">We'll reposition your business in the marketplace so that it resonates with your target market.&nbsp; We'll then help you implement powerful online and offline lead generation and sales strategies.</p>

  <div class="abs thumb" style="top:442px;height:69px;background:linear-gradient(135deg,#c9b9a3,#6d5a48 60%,#3e3a38)" role="img" aria-label="Photo of two businessmen celebrating"></div>
  <div class="abs pill" style="left:159px;top:442px">Marketing &amp; PR Strategy</div>
  <p class="abs svc-text" style="left:158px;top:469px">Learn more about how we can help build your customer base and penetrate new markets.</p>
  <a class="abs more" style="left:158px;top:500px">Click here to find out more</a>

  <div class="abs thumb" style="top:527px;height:69px;background:linear-gradient(#fafafa,#e2e2e2)" role="img" aria-label="Photo of darts hitting a target"></div>
  <div class="abs pill" style="left:159px;top:527px">Campaign Design &amp; Execution</div>
  <p class="abs svc-text" style="left:159px;top:554px">Seeking a marketing plan that works?&nbsp; Learn more about how we implement our powerful marketing strategies.</p>
  <a class="abs more" style="left:159px;top:585px">Click here to find out more</a>

  <div class="abs thumb" style="top:613px;height:73px;background:radial-gradient(circle at 45% 45%,#e8e8e8,#f8f8f8 70%)" role="img" aria-label="Illustration of a head with colourful gears"></div>
  <div class="abs pill" style="left:159px;top:612px">Creative</div>
  <p class="abs svc-text" style="left:159px;top:639px;width:252px">Quickpine design &amp; develop brochures, podcasts, vodcasts, advertisements, e-marketing campaigns, direct marketing &amp; promotional videos</p>
  <a class="abs more" style="left:159px;top:681px">Click here to find out more</a>

  <div class="abs thumb" style="top:705px;height:74px;background:radial-gradient(circle at 50% 40%,#e6e6e6,#fdfdfd 60%)" role="img" aria-label="Illustration of a light bulb with an at sign"></div>
  <div class="abs pill" style="left:159px;top:704px">Web Site Design &amp; Online Strategy</div>
  <p class="abs svc-text" style="left:159px;top:731px">What is your web site saying about your business?&nbsp; Learn how quickpine can build a new web site for your business that generates enquiries and convert sales.</p>
  <a class="abs more" style="left:159px;top:773px">Click here to find out more</a>

  <div class="abs tile" style="left:42px;top:797px">
    <h3>Want</h3>
    <p>a Web solution<br>that actually Builds <b>Business</b>?</p>
    <small><b>Click here</b> to learn more about our Web<br>Development &amp; on line Marketing programs.</small>
  </div>
  <div class="abs tile" style="left:233px;top:798px">
    <h3>Could</h3>
    <p>a Video Presentation make all the<br>Difference to Your <b>Business</b>?</p>
    <small><b>Click here</b> to learn more about our Media<br>Production solutions</small>
  </div>
  <div class="abs tile" style="left:42px;top:917px">
    <h3>Feel</h3>
    <p>Like You're Not in Control of Your<br><b>Business</b>?</p>
    <small><b>Click here</b> to learn more about our Web<br>Development &amp; on line Marketing programs.</small>
  </div>
  <div class="abs tile" style="left:233px;top:917px">
    <h3>Looking</h3>
    <p>to Fine Tune Your <b>Sales</b> Team?</p>
    <small><b>Click here</b> &nbsp;to learn more about our Sales Force<br>Effectiveness programs</small>
  </div>
</main>

<!-- sidebar -->
<aside>
  <div class="abs box assess" style="top:229px;height:147px"></div>
  <div class="abs badge" role="img" aria-label="Free badge"></div>
  <div class="abs box-title" style="left:480px;top:239px">Marketing Assessment</div>
  <span class="abs label" style="left:445px;top:271px">Name</span>
  <span class="abs label" style="left:445px;top:298px">Company Name</span>
  <span class="abs label" style="left:445px;top:325px">Email</span>
  <div class="abs input" style="top:267px"></div>
  <div class="abs input" style="top:293px"></div>
  <div class="abs input" style="top:320px"></div>
  <div class="abs btn blue" style="left:520px;top:348px;width:116px">GET YOUR ASSESSMENT</div>

  <div class="abs box" style="top:399px;height:117px"></div>
  <div class="abs box-title" style="left:445px;top:404px"><b>Join</b> our mailing list</div>
  <span class="abs label" style="left:445px;top:440px">Your Name</span>
  <span class="abs label" style="left:445px;top:466px">Email</span>
  <div class="abs input" style="top:434px"></div>
  <div class="abs input" style="top:461px"></div>
  <div class="abs btn orange" style="left:520px;top:490px;width:58px">SUBSCRIBE</div>

  <div class="abs box" style="top:541px;height:133px"></div>
  <div class="abs box-title" style="left:446px;top:548px"><b>What</b> are you looking for</div>
  <ul class="looking">
    <li style="top:580px">I want to increase brand awareness</li>
    <li style="top:599px">I want greater lead generation</li>
    <li style="top:617px">I want a powerful online strategy</li>
    <li style="top:635px">I want to launch a new product or service</li>
    <li style="top:653px">I want a marketing overhaul</li>
  </ul>

  <div class="abs box" style="top:697px;height:174px"></div>
  <div class="abs video" role="img" aria-label="Video still of a presenter speaking on stage"></div>
  <div class="abs video-head"><span class="av"></span>Quick Pine<small>from <span>Dale Marsh</span></small></div>
  <svg class="abs" style="left:447px;top:833px" width="188" height="30" viewBox="0 0 188 30" aria-hidden="true">
    <rect x="0" y="0" width="188" height="30" fill="#000" opacity=".55"/>
    <rect x="4" y="4" width="34" height="22" fill="#111"/>
    <path d="M16 9 L27 15 L16 21 Z" fill="#fff"/>
    <rect x="50" y="12" width="74" height="6" fill="none" stroke="#aaa"/>
    <rect x="48" y="1" width="20" height="7" fill="#fff"/>
    <text x="58" y="7" font-size="5.5" text-anchor="middle" font-family="Open Sans" fill="#000">00:44</text>
    <g fill="#3fb2ef"><rect x="132" y="11" width="2" height="8"/><rect x="136" y="11" width="2" height="8"/><rect x="140" y="11" width="2" height="8"/><rect x="144" y="11" width="2" height="8"/><rect x="148" y="11" width="2" height="8"/></g>
    <path d="M170 11h3v1h-2v2h-1zM180 11h-3v1h2v2h1zM170 19h3v-1h-2v-2h-1zM180 19h-3v-1h2v-2h1z" fill="#fff"/>
  </svg>

  <div class="abs box" style="top:895px;height:129px"></div>
  <div class="abs box-title" style="left:446px;top:902px"><b>Recent</b> media</div>
  <div class="abs media-item" style="top:934px"><svg width="10" height="10" viewBox="0 0 10 10"><rect x=".5" y="1.5" width="7" height="8" fill="#fff" stroke="#3a7bc8"/><path d="M4 7 L9 1.5" stroke="#e88a00" stroke-width="1.6"/></svg><span>Podcast on 7 Ways to<br>Improve your marketing</span></div>
  <div class="abs media-item" style="top:965px"><svg width="10" height="10" viewBox="0 0 10 10"><rect x=".5" y="1.5" width="7" height="8" fill="#fff" stroke="#3a7bc8"/><path d="M4 7 L9 1.5" stroke="#e88a00" stroke-width="1.6"/></svg><span>Article on Why Most Marketing Fails</span></div>
  <div class="abs media-item" style="top:985px"><svg width="10" height="10" viewBox="0 0 10 10"><rect x=".5" y="1.5" width="7" height="8" fill="#fff" stroke="#3a7bc8"/><path d="M4 7 L9 1.5" stroke="#e88a00" stroke-width="1.6"/></svg><span>Podcast interview with Mira Calloway</span></div>
  <a class="abs more" style="left:571px;top:1007px">More Media Items</a>
</aside>

<!-- footer -->
<div class="abs bubble" style="left:513px;top:1108px;width:94px">SEND TO A FRIEND</div>
<div class="abs bubble" style="left:616px;top:1108px;width:30px">RSS</div>
<footer class="abs footer">
  <div class="abs site">WWW.QUICKPINE.COM</div>
  <div class="abs contact">(02) 9418 3307 &nbsp; Location: Sydney Australia</div>
  <nav>
    <a href="#" style="left:231px">HOME</a><i style="left:262px">.</i>
    <a href="#" style="left:273px">WHAT WE'RE WORKING ON</a><i style="left:388px">.</i>
    <a href="#" style="left:398px">ABOUT US</a><i style="left:446px">.</i>
    <a href="#" style="left:457px">MEDIA</a><i style="left:490px">.</i>
    <a href="#" style="left:500px">BLOG</a><i style="left:530px">.</i>
    <a href="#" style="left:540px">CONTACT US</a><i style="left:597px">.</i>
    <a class="map" href="#" style="left:608px">SITE MAP</a>
  </nav>
</footer>
<div class="abs legal"><span class="abs" style="left:505px;top:0">Copyright © quickpine 2009</span><span class="abs" style="left:607px;top:0">Legal politics</span></div>

</body>
</html>
```